Security Cheat Sheets

We are after a nicely presented easy to follow cheat sheet around security such as Phishing and scams and acceptable use we can send to our clients for awareness.
The example Cheat Sheets is some info we would like (was something i downloaded from the internet so do not copy verbatim but has some good content ideas we would like to use) and a very simple example i prepared plus our logos etc.

```html
<!DOCTYPE html>
<html lang="en">
<head>
<meta charset="utf-8">
<title>Phishing and Scams – Awareness Cheat Sheet</title>
<link rel="stylesheet" href="https://fonts.googleapis.com/css2?family=Montserrat:wght@600;700;800;900&family=Open+Sans:wght@400;600;700&display=swap">
<style>
:root{
  --navy:#071634;
  --navy-deep:#040c22;
  --blue:#1b5fd0;
  --blue-glow:#2f8cff;
  --cyan:#3fc6ff;
  --green:#5fd12e;
  --green-dark:#3ea414;
  --red:#e12b2b;
  --white:#ffffff;
  --ink:#16223d;
  --row-line:#c9d3e6;
  --muted:#d6e3ff;
}
*{box-sizing:border-box;margin:0;padding:0}
html,body{width:1200px;height:2268px;overflow:hidden;background:var(--navy-deep)}
.sheet{
  position:relative;width:1200px;height:2268px;overflow:hidden;
  font-family:"Open Sans",Arial,sans-serif;color:var(--white);
  background:
    radial-gradient(ellipse 700px 500px at 900px 230px, rgba(47,140,255,.45), transparent 70%),
    radial-gradient(ellipse 600px 400px at 150px 2000px, rgba(47,140,255,.25), transparent 70%),
    linear-gradient(180deg,#0a1f4a 0%,var(--navy) 40%,var(--navy-deep) 100%);
}
.brand{position:absolute;left:60px;top:56px;display:flex;align-items:center;gap:16px}
.brand-mark{width:46px;height:46px;background:var(--blue-glow);border-radius:6px}
.brand-name{font-family:"Montserrat",Arial,sans-serif;font-weight:700;font-size:30px;letter-spacing:1px;color:var(--white)}
.brand-tag{position:absolute;left:122px;top:104px;font-size:18px;color:var(--muted)}
.hero-art{
  position:absolute;left:690px;top:30px;width:470px;height:430px;border-radius:20px;
  background:radial-gradient(circle at 50% 45%, rgba(120,210,255,.75) 0%, rgba(47,140,255,.45) 35%, rgba(10,40,100,0) 72%);
}
.title{position:absolute;left:60px;top:200px;font-family:"Montserrat",Arial,sans-serif;font-weight:900;font-size:124px;line-height:1;letter-spacing:1px;text-transform:uppercase}
.title span{display:block}
.pills{position:absolute;left:60px;top:478px;display:flex;gap:18px}
.pill{background:var(--green);color:var(--navy);font-family:"Montserrat",Arial,sans-serif;font-weight:800;font-size:28px;padding:12px 28px;border-radius:30px;white-space:nowrap}
.panel{position:absolute;left:40px;top:570px;width:1120px;height:990px;background:var(--white);border-radius:18px;color:var(--ink);padding:26px 36px}
.panel-title{font-family:"Montserrat",Arial,sans-serif;font-weight:900;font-size:44px;color:var(--navy);text-transform:uppercase}
.section-bar{margin:18px 0 14px;background:var(--green);color:var(--navy);font-family:"Montserrat",Arial,sans-serif;font-weight:800;font-size:30px;padding:10px 22px;border-radius:8px}
.check-row{display:flex;align-items:center;gap:20px;border:2px solid var(--row-line);border-radius:12px;padding:12px 18px;margin-bottom:12px;font-size:22px;line-height:1.35;min-height:76px}
.check-row svg{flex:0 0 44px}
.hacked-bar{position:absolute;left:290px;top:1580px;width:620px;background:var(--green);color:var(--navy);text-align:center;font-family:"Montserrat",Arial,sans-serif;font-weight:900;font-size:32px;padding:10px;border-radius:8px;text-transform:uppercase}
.info-card{position:absolute;top:1650px;width:540px;height:250px;border-radius:16px;background:linear-gradient(135deg,#1e63d8,#0e3a92);border:2px solid var(--blue-glow);padding:24px;display:flex;gap:18px;align-items:center}
.info-card.left{left:40px}.info-card.right{left:620px}
.info-card p{font-size:21px;line-height:1.42;flex:1}
.card-art{flex:0 0 150px;height:150px;border-radius:12px;background:linear-gradient(160deg,rgba(63,198,255,.7),rgba(14,58,146,.4))}
.action{position:absolute;left:60px;top:1950px;width:1080px}
.action h2{font-family:"Montserrat",Arial,sans-serif;font-weight:900;font-size:56px;color:var(--green);text-transform:uppercase}
.action p{margin-top:10px;font-size:24px;line-height:1.45;width:760px}
.contact{position:absolute;left:60px;top:2150px;width:1080px;display:flex;align-items:flex-end;justify-content:space-between;gap:24px}
.contact-label{font-family:"Montserrat",Arial,sans-serif;font-weight:700;font-size:18px;text-transform:uppercase;color:var(--muted);display:block;margin-bottom:6px}
.phone{display:flex;align-items:center;gap:12px;white-space:nowrap}
.phone strong{font-family:"Montserrat",Arial,sans-serif;font-weight:900;font-size:40px;line-height:1}
.web{font-family:"Montserrat",Arial,sans-serif;font-weight:700;font-size:20px;white-space:nowrap;padding-bottom:8px}
.divider{flex:0 0 2px;width:2px;height:44px;background:var(--blue-glow)}
</style>
</head>
<body>
<main class="sheet">
  <header>
    <div class="brand"><div class="brand-mark"></div><div class="brand-name">NEXORA TECHNOLOGY</div></div>
    <div class="brand-tag">"ICT Solutions &amp; Engineering"</div>
    <div class="hero-art" role="img" aria-label="Glowing digital padlock and security shield on a blue circuit background"></div>
    <h1 class="title"><span>Phishing</span><span>and Scams</span></h1>
    <div class="pills">
      <div class="pill">How to detect?</div>
      <div class="pill">What to do?</div>
      <div class="pill">How to avoid being scammed?</div>
    </div>
  </header>

  <section class="panel">
    <h2 class="panel-title">Detection and Awareness</h2>
    <div class="section-bar">Look at the senders email address</div>
    <div class="check-row">
      <svg width="44" height="44" viewBox="0 0 44 44"><circle cx="22" cy="22" r="20" fill="var(--green)"/><path d="M12 23l7 7 13-15" stroke="#fff" stroke-width="5" fill="none" stroke-linecap="round" stroke-linejoin="round"/></svg>
      <span>Senders from Email address is from your domain or a trusted domain</span>
    </div>
    <div class="check-row">
      <svg width="44" height="44" viewBox="0 0 44 44"><circle cx="22" cy="22" r="20" fill="var(--red)"/><path d="M14 14l16 16M30 14L14 30" stroke="#fff" stroke-width="5" stroke-linecap="round"/></svg>
      <span>Senders from Email address is from a random email address or freemail like Mailzo, Postbox or similar account</span>
    </div>
    <div class="check-row">
      <svg width="44" height="44" viewBox="0 0 44 44"><circle cx="22" cy="22" r="20" fill="var(--red)"/><path d="M14 14l16 16M30 14L14 30" stroke="#fff" stroke-width="5" stroke-linecap="round"/></svg>
      <span>Senders from Email address is from the CEO / Accounts etc but the address is not your corporate domain, for example ceo@postbox.com</span>
    </div>
    <div class="check-row">
      <svg width="44" height="44" viewBox="0 0 44 44"><circle cx="22" cy="22" r="20" fill="var(--red)"/><path d="M14 14l16 16M30 14L14 30" stroke="#fff" stroke-width="5" stroke-linecap="round"/></svg>
      <span>Senders from Email address is from a random email address or freemail like Mailzo or Postbox account</span>
    </div>
    <div class="check-row">
      <svg width="44" height="44" viewBox="0 0 44 44"><circle cx="22" cy="22" r="20" fill="var(--red)"/><path d="M14 14l16 16M30 14L14 30" stroke="#fff" stroke-width="5" stroke-linecap="round"/></svg>
      <span>Sender is pretending to be an internal staff member but the email body has the "External Mail" pink bar warning</span>
    </div>
    <div class="section-bar">Contain a link to reset password or Scare Tactic</div>
    <div class="check-row">
      <svg width="44" height="44" viewBox="0 0 44 44"><circle cx="22" cy="22" r="20" fill="var(--red)"/><path d="M14 14l16 16M30 14L14 30" stroke="#fff" stroke-width="5" stroke-linecap="round"/></svg>
      <span>Vendrix, the National Revenue Office and others will not ask you to click a link to reset your password</span>
    </div>
    <div class="check-row">
      <svg width="44" height="44" viewBox="0 0 44 44"><circle cx="22" cy="22" r="20" fill="var(--red)"/><path d="M14 14l16 16M30 14L14 30" stroke="#fff" stroke-width="5" stroke-linecap="round"/></svg>
      <span>Vendrix, NetGrid and others do not monitor your computer or network and advise you they detected an error, click a link to resolve</span>
    </div>
  </section>

  <section>
    <div class="hacked-bar">Does this mean I was hacked</div>
    <div class="info-card left">
      <p>There is a very strong likelihood you were not hacked. Scammers will obtain your email address from websites, public profiles or from someone's mailbox.</p>
      <div class="card-art" role="img" aria-label="Laptop with a warning symbol on screen"></div>
    </div>
    <div class="info-card right">
      <p>Scammers are pretending to be someone else (phishing) or use a scare tactic to trick you into giving them your information / passwords or other fraud attempts.</p>
      <div class="card-art" role="img" aria-label="Laptop showing a hooked login form"></div>
    </div>
  </section>

  <section class="action">
    <h2>What should I do</h2>
    <p>You can safely ignore and delete the email and if in doubt, please contact Nexora who can check and advise further.</p>
  </section>

  <footer class="contact">
    <div>
      <span class="contact-label">Contact us</span>
      <div class="phone">
        <svg width="40" height="40" viewBox="0 0 24 24"><circle cx="12" cy="12" r="12" fill="var(--green)"/><path d="M8.2 6.5l1.8-.3 1 2.6-1.2 1a7 7 0 003.4 3.4l1-1.2 2.6 1-.3 1.8c-.2.8-1 1.2-1.8 1.1A9 9 0 017.1 8.3c-.1-.8.3-1.6 1.1-1.8z" fill="var(--navy)"/></svg>
        <strong>1300 555 014</strong>
      </div>
    </div>
    <div class="divider"></div>
    <div class="web">WWW.NEXORATECH.COM.AU</div>
    <div class="divider"></div>
    <div class="web">HELP@NEXORATECH.COM.AU</div>
  </footer>
</main>
</body>
</html>
```